Torvane Systems*

Stationary design including business cards, letter heads, envelops and email signatures using our new logo

Target Market(s)

Innovative Technologies

Industry/Entity Type

Defense Contracting

Font styles to use
Sans Serif

```html
<!DOCTYPE html>
<html lang="en">
<head>
<meta charset="utf-8">
<title>Torvane Systems – Business Card</title>
<link rel="stylesheet" href="https://fonts.googleapis.com/css2?family=Roboto:wght@300;400;500&family=Oswald:wght@400&display=swap">
<style>
  :root {
    --backdrop: #e4e4e2;
    --card: #2c2c2c;
    --card-back: #232323;
    --ink: #f2f2f2;
    --ink-soft: #cfcfcf;
    --rule: #bdbdbd;
  }
  * { box-sizing: border-box; margin: 0; padding: 0; }
  html, body { width: 1200px; height: 801px; overflow: hidden; }
  body {
    background: var(--backdrop);
    font-family: "Roboto", Arial, sans-serif;
    color: var(--ink);
    display: flex;
    align-items: center;
    justify-content: center;
    gap: 60px;
  }
  .card {
    position: relative;
    width: 525px;
    height: 300px;
    border-radius: 4px;
    box-shadow: 0 8px 24px rgba(0,0,0,0.25);
  }
  .card--front { background: var(--card); }
  .card--back { background: var(--card-back); }

  .brand {
    position: absolute;
    display: flex;
    align-items: center;
    gap: 10px;
    font-family: "Oswald", Arial, sans-serif;
    font-weight: 400;
    color: var(--ink);
    letter-spacing: 0.5px;
    white-space: nowrap;
  }
  .brand__mark {
    width: 14px; height: 14px;
    border: 1.5px solid var(--ink);
  }
  .card--front .brand { top: 44px; right: 34px; font-size: 26px; }
  .card--front .brand-rule {
    position: absolute; top: 92px; left: 34px; right: 34px;
    height: 1px; background: var(--rule);
  }
  .address {
    position: absolute; top: 108px; right: 34px;
    text-align: right; font-size: 14px; font-weight: 300;
    line-height: 1.35; color: var(--ink-soft);
  }
  .person { position: absolute; left: 34px; bottom: 40px; }
  .person__name { font-size: 19px; font-weight: 500; }
  .person__title { font-size: 13px; font-weight: 300; color: var(--ink-soft); margin-top: 2px; }
  .person__rule { width: 240px; height: 1px; background: var(--rule); margin: 10px 0 10px; }
  .contacts { list-style: none; font-size: 14px; font-weight: 300; }
  .contacts li { display: flex; align-items: center; gap: 10px; line-height: 1.45; }
  .contacts svg { width: 11px; height: 11px; flex: none; }

  .pattern-field {
    position: absolute; inset: 0;
    border-radius: 4px;
    background: linear-gradient(120deg, #1f1f1f 0%, #2a2a2a 55%, #353535 100%);
  }
  .card--back .brand { top: 50%; right: 36px; transform: translateY(-50%); font-size: 30px; }
</style>
</head>
<body>
  <section class="card card--front">
    <div class="brand"><span class="brand__mark"></span>Torvane Systems</div>
    <div class="brand-rule"></div>
    <p class="address">Your address, city<br>state, ZIP 0000</p>
    <div class="person">
      <h1 class="person__name">Daniel Hartley</h1>
      <p class="person__title">Manager</p>
      <div class="person__rule"></div>
      <ul class="contacts">
        <li>
          <svg viewBox="0 0 12 12" aria-hidden="true"><path d="M2.5 1h2l1 2.5-1.3 1a6 6 0 0 0 3.3 3.3l1-1.3 2.5 1v2c0 .6-.5 1-1 1A9.5 9.5 0 0 1 1.5 2c0-.5.4-1 1-1z" fill="#f2f2f2"/></svg>
          555-014-2100
        </li>
        <li>
          <svg viewBox="0 0 12 12" aria-hidden="true"><rect x="0.75" y="2.25" width="10.5" height="7.5" fill="none" stroke="#f2f2f2" stroke-width="1.2"/><path d="M1 2.7 6 6.6l5-3.9" fill="none" stroke="#f2f2f2" stroke-width="1.2"/></svg>
          d.hartley@torvanemail.com
        </li>
        <li>
          <svg viewBox="0 0 12 12" aria-hidden="true"><circle cx="6" cy="6" r="5.3" fill="none" stroke="#f2f2f2" stroke-width="1.1"/><path d="M.8 6h10.4M6 .7c2.6 2.8 2.6 7.8 0 10.6M6 .7c-2.6 2.8-2.6 7.8 0 10.6" fill="none" stroke="#f2f2f2" stroke-width="0.9"/></svg>
          www.torvanesystems.com
        </li>
      </ul>
    </div>
  </section>

  <section class="card card--back">
    <div class="pattern-field" role="img" aria-label="Repeating tone-on-tone brand symbol pattern in dark grey"></div>
    <div class="brand"><span class="brand__mark"></span>Torvane Systems</div>
  </section>
</body>
</html>
```